KerrLow Farm

Need a nice simple clean double sided business card that has our logo and info on:
Kerr Low Farm
Martin & Felicity Kerr Low
kerrlowfarm@mailbarn.example
Martin: 1-780-555-0148
Felicity: 1-780-555-0193
Instagram @ kerrlow_farm

Contact Information for Business Card

Martin & Felicity Kerr Low kerrlowfarm@mailbarn.example Martin: 1-780-555-0148 Felicity: 1-780-555-0193

```html
<!DOCTYPE html>
<html lang="en">
<head>
<meta charset="utf-8">
<title>Kerr Low Farm — Business Card</title>
<link rel="stylesheet" href="https://fonts.googleapis.com/css2?family=Cinzel:wght@700&family=Arimo:wght@400&display=swap">
<style>
  :root {
    --backdrop: #e7e4df;
    --card-black: #151515;
    --card-white: #ffffff;
    --farm-green: #5a9e32;
    --wheat-orange: #f0a428;
    --text-white: #ffffff;
    --text-dark: #2a2a2a;
  }
  * { box-sizing: border-box; margin: 0; padding: 0; }
  html, body { width: 1200px; height: 913px; overflow: hidden; }
  body {
    background: var(--backdrop);
    display: flex;
    flex-direction: column;
    align-items: center;
    justify-content: center;
    gap: 38px;
  }
  .card {
    position: relative;
    width: 700px;
    height: 400px;
    box-shadow: 0 6px 18px rgba(0,0,0,0.18);
    overflow: hidden;
  }
  .card--front { background: var(--card-black); }
  .card--back { background: var(--card-white); }

  .company-name {
    position: absolute;
    left: 0; right: 0;
    text-align: center;
    font-family: "Arimo", sans-serif;
    font-weight: 400;
    font-size: 36px;
    letter-spacing: 0.5px;
  }
  .card--front .company-name { top: 178px; color: var(--text-white); }
  .card--back .company-name { top: 100px; color: var(--text-dark); }

  .contact-band {
    position: absolute;
    left: 0; right: 0;
    top: 222px;
    height: 112px;
    background: var(--farm-green);
    border-top: 3px solid var(--wheat-orange);
    border-bottom: 3px solid var(--wheat-orange);
    display: flex;
    align-items: center;
    justify-content: space-between;
    padding: 0 40px;
  }
  .owners {
    font-family: "Cinzel", serif;
    font-weight: 700;
    font-size: 22px;
    line-height: 1.2;
    text-transform: uppercase;
  }
  .owners__first { color: var(--text-white); }
  .owners__last { color: var(--wheat-orange); }

  .contact-list { list-style: none; }
  .contact-list li {
    display: flex;
    align-items: center;
    gap: 10px;
    font-family: "Arimo", sans-serif;
    font-size: 15px;
    line-height: 1.45;
    color: var(--text-white);
  }
  .contact-list svg { width: 13px; height: 13px; flex: none; }
</style>
</head>
<body>
  <section class="card card--front" aria-label="Card front">
    <div class="company-name">Kerr Low Farm</div>
  </section>

  <section class="card card--back" aria-label="Card back">
    <div class="company-name">Kerr Low Farm</div>

    <div class="contact-band">
      <div class="owners">
        <div class="owners__first">Martin &amp; Felicity</div>
        <div class="owners__last">Kerr Low</div>
      </div>
      <ul class="contact-list">
        <li>
          <svg viewBox="0 0 16 16"><path fill="#f0a428" d="M3.5 1l3 3-1.6 1.8a9 9 0 0 0 5.3 5.3L12 9.5l3 3-2 2.5C7 15 1 9 1 3z"/></svg>
          1-780-555-0148 (Martin)
        </li>
        <li>
          <svg viewBox="0 0 16 16"><path fill="#f0a428" d="M3.5 1l3 3-1.6 1.8a9 9 0 0 0 5.3 5.3L12 9.5l3 3-2 2.5C7 15 1 9 1 3z"/></svg>
          1-780-555-0193 (Felicity)
        </li>
        <li>
          <svg viewBox="0 0 16 16"><rect x="1" y="3" width="14" height="10" fill="#f0a428"/><path d="M1 3l7 6 7-6" fill="none" stroke="#5a9e32" stroke-width="1.5"/></svg>
          kerrlowfarm@mailbarn.example
        </li>
        <li>
          <svg viewBox="0 0 16 16"><circle cx="8" cy="8" r="6" fill="none" stroke="#f0a428" stroke-width="2"/></svg>
          @kerrlow_farm
        </li>
      </ul>
    </div>
  </section>
</body>
</html>
```